Willowbay Dental Centre Tarrawin Opening special DL flyer

dl flyer design with opening special offers and services provide and the location we are in

opening special offer : exam, clean and flouride treatment for $129 or No Gap if with Health Insurance.
$99 mouth guards for footy season
Emergency Dental Appointments Available everyday!!!
Open on Saturdays

Services:
6 monthly Maintainence
CAD/CAM Dentistry
Conscious Sedation
Cosmetic Dentistry
Crowns and Bridges
Dental Implant
Fissure Sealants
Tresluxa
Periodontal Treatment
Root Canal Treatment
Teeth Whitening
Tooth Coloured Fillings
Tooth Replacement

Interest Free Payment Plans Available

Address: Willowbay Dental Centre Tarrawin
318D, Pellam Street, Tarrawin - 4587
Ph: 07-5019 4427
email: admin@willowbaydentalcentretarrawin.com.au
Website: www.willowbaydentalcentretarrawin.com.au

Opening Hours:
Mon/Wed 8:30AM - 5PM
Thursday 9AM - 7PM
Friday 9AM - 5PM
Saturday 9AM - 1PM

Target Market(s)

local community

Industry/Entity Type

Dental

Font styles to use
Serif

Requirements
Must have
• all the above details

```html
<!DOCTYPE html>
<html lang="en">
<head>
<meta charset="utf-8">
<title>Willowbay Dental Centre Tarrawin – Opening Special DL Flyer</title>
<link rel="stylesheet" href="https://fonts.googleapis.com/css2?family=Open+Sans:ital,wght@0,400;0,600;0,700;1,700&family=Libre+Baskerville:wght@700&display=swap">
<style>
  :root {
    --green: #8aa957;
    --charcoal: #252525;
    --ink: #1d1d1d;
    --white: #ffffff;
    --sky: #dcedf7;
    --backdrop: #e9e9e9;
    --sans: "Open Sans", Arial, sans-serif;
    --serif: "Libre Baskerville", Georgia, serif;
  }
  * { box-sizing: border-box; margin: 0; padding: 0; }
  html, body { width: 1200px; height: 1188px; overflow: hidden; }
  body { background: var(--backdrop); font-family: var(--sans); color: var(--ink); position: relative; }

  .flyer-side {
    position: absolute; left: 88px; width: 1024px; height: 482px;
    background: var(--white); overflow: hidden;
    box-shadow: 0 6px 18px rgba(0,0,0,.25);
  }
  .flyer-front { top: 70px; }
  .flyer-back { top: 636px; }
  .abs { position: absolute; }
  .shapes { position: absolute; inset: 0; width: 100%; height: 100%; }

  /* ---------- front ---------- */
  .family-photo {
    left: 0; top: 0; width: 660px; height: 330px;
    background: linear-gradient(90deg, #c9a98c 0%, #d8c0a8 35%, #e9ddd0 70%, rgba(255,255,255,0) 100%),
                linear-gradient(180deg, #a9c6d4 0%, #e8e2da 60%);
  }
  .offer-headline {
    right: 16px; top: 26px; font-size: 38px; font-weight: 400;
    letter-spacing: .5px; color: var(--ink);
  }
  .offer-headline strong { font-weight: 700; }
  .offer-box {
    left: 630px; top: 98px; width: 394px; height: 230px;
    background: var(--green); border-radius: 20px 0 0 0; color: var(--white);
  }
  .offer-exam { left: 20px; top: 38px; width: 250px; }
  .offer-exam .lead { font-size: 16px; font-weight: 700; line-height: 1.3; text-transform: uppercase; }
  .offer-exam .note { font-size: 14.5px; line-height: 1.3; }
  .price { font-family: var(--serif); font-weight: 700; color: var(--white); }
  .price-exam { left: 278px; top: 46px; font-size: 40px; }
  .divider-v { width: 1.5px; background: rgba(255,255,255,.85); }
  .divider-exam { left: 266px; top: 40px; height: 62px; }
  .divider-h { left: 20px; right: 0; top: 132px; height: 1px; background: rgba(255,255,255,.5); }
  .price-guard { left: 30px; top: 170px; font-size: 36px; }
  .divider-guard { left: 108px; top: 165px; height: 52px; }
  .offer-guard { left: 122px; top: 170px; font-size: 16px; font-weight: 700; line-height: 1.3; text-transform: uppercase; }

  .brand { display: flex; align-items: center; gap: 10px; }
  .brand-dot { width: 34px; height: 34px; border-radius: 50%; background: var(--green); flex: none; }
  .brand-name { font-size: 17px; font-weight: 600; line-height: 1.15; color: var(--green); text-transform: uppercase; }
  .front-brand { left: 24px; top: 372px; }

  .icon-badge {
    width: 30px; height: 30px; border-radius: 50%; background: var(--green);
    display: flex; align-items: center; justify-content: center; color: var(--white);
    font-size: 11px; font-weight: 700; flex: none;
  }
  .icon-badge svg { width: 16px; height: 16px; }
  .front-contact { top: 382px; display: flex; align-items: center; gap: 10px; color: var(--white); }
  .front-phone { left: 282px; font-size: 26px; font-weight: 700; }
  .front-emergency { left: 540px; font-size: 14px; line-height: 1.35; }
  .front-finance { left: 830px; font-size: 14px; line-height: 1.35; }

  .web-strip {
    left: 0; top: 442px; width: 1024px; height: 40px; background: var(--sky);
    display: flex; align-items: center; justify-content: center;
    font-size: 17px; font-weight: 700; letter-spacing: 3.4px; color: var(--ink);
  }

  /* ---------- back ---------- */
  .patient-photo {
    left: 240px; top: 0; width: 300px; height: 482px;
    background: linear-gradient(90deg, rgba(255,255,255,0) 0%, #eadfd6 30%, #d7c2b4 65%, #cfd9de 100%);
  }
  .clinic-photo {
    left: 520px; top: 0; width: 320px; height: 320px;
    background: linear-gradient(135deg, #e9e4da 0%, #cfc3ad 40%, #7d8fa4 75%, #e8eef2 100%);
  }
  .services-title { left: 20px; top: 22px; font-size: 30px; font-weight: 700; color: var(--ink); }
  .services-list { left: 20px; top: 72px; list-style: none; }
  .services-list li {
    position: relative; padding-left: 22px; font-size: 17px; font-weight: 600;
    line-height: 26.5px; color: var(--ink);
  }
  .services-list li::before {
    content: ""; position: absolute; left: 2px; top: 11px; width: 6px; height: 6px;
    border-radius: 50%; background: var(--green);
  }
  .hours { left: 860px; top: 80px; width: 156px; }
  .hours h3 { font-size: 15px; font-weight: 700; margin-bottom: 8px; padding-left: 20px; }
  .hours table { border-collapse: collapse; font-size: 12.5px; font-weight: 600; }
  .hours td { padding: 1px 0; white-space: nowrap; }
  .hours td:first-child { padding-right: 8px; }
  .saturday-note { left: 860px; top: 190px; font-size: 15px; font-weight: 700; font-style: italic; }
  .back-phone-icon { left: 990px; top: 218px; width: 28px; height: 28px; }
  .back-phone { right: 16px; top: 250px; font-size: 26px; font-weight: 700; line-height: 1.2; }

  .back-brand { left: 548px; top: 324px; }
  .contact-row { left: 552px; display: flex; align-items: center; gap: 12px; color: var(--white); font-size: 14px; line-height: 1.35; }
  .contact-row .icon-badge { width: 24px; height: 24px; }
  .contact-row .icon-badge svg { width: 13px; height: 13px; }
  .contact-address { top: 372px; }
  .contact-email { top: 416px; }
  .contact-web { top: 446px; color: var(--green); }
</style>
</head>
<body>

<section class="flyer-side flyer-front">
  <div class="abs family-photo" role="img" aria-label="Photo of a smiling family of four on a beach"></div>

  <svg class="shapes" viewBox="0 0 1024 482" aria-hidden="true">
    <path d="M0,236 C260,318 520,338 1024,322 L1024,342 C520,356 260,348 0,282 Z" fill="var(--green)"/>
    <path d="M0,282 C260,348 520,356 1024,342 L1024,442 L0,442 Z" fill="var(--charcoal)"/>
  </svg>

  <h1 class="abs offer-headline">OPENING <strong>SPECIAL OFFER</strong></h1>

  <div class="abs offer-box">
    <div class="abs offer-exam">
      <p class="lead">Exam, clean and<br>flouride treatment for</p>
      <p class="note">Or No Gap If With Health<br>Insurance.</p>
    </div>
    <div class="abs divider-v divider-exam"></div>
    <div class="abs price price-exam">$129</div>
    <div class="abs divider-h"></div>
    <div class="abs price price-guard">$99</div>
    <div class="abs divider-v divider-guard"></div>
    <p class="abs offer-guard">Mouth guards for<br>footy season</p>
  </div>

  <div class="abs brand front-brand">
    <span class="brand-dot"></span>
    <span class="brand-name">Willowbay Dental<br>Centre</span>
  </div>

  <div class="abs front-contact front-phone">
    <span class="icon-badge"><svg viewBox="0 0 24 24"><path fill="#fff" d="M6.6 10.8a15 15 0 0 0 6.6 6.6l2.2-2.2a1 1 0 0 1 1-.25 11.4 11.4 0 0 0 3.6.57 1 1 0 0 1 1 1V20a1 1 0 0 1-1 1A17 17 0 0 1 3 4a1 1 0 0 1 1-1h3.5a1 1 0 0 1 1 1c0 1.25.2 2.45.57 3.57a1 1 0 0 1-.25 1z"/></svg></span>
    <span>07-5019 4427</span>
  </div>
  <div class="abs front-contact front-emergency">
    <span class="icon-badge"><svg viewBox="0 0 24 24"><rect x="4" y="5" width="16" height="15" rx="2" fill="none" stroke="#fff" stroke-width="2"/><path d="M4 9h16M8 3v4M16 3v4" stroke="#fff" stroke-width="2"/></svg></span>
    <span>Emergency Dental Appointments<br>Available everyday!</span>
  </div>
  <div class="abs front-contact front-finance">
    <span class="icon-badge">0%</span>
    <span>Interest Free Payment<br>Plans Available</span>
  </div>

  <div class="abs web-strip">www.willowbaydentalcentretarrawin.com.au</div>
</section>

<section class="flyer-side flyer-back">
  <div class="abs patient-photo" role="img" aria-label="Photo of a patient in a dental chair with a dentist"></div>
  <div class="abs clinic-photo" role="img" aria-label="Photo of the clinic reception area"></div>

  <svg class="shapes" viewBox="0 0 1024 482" aria-hidden="true">
    <path d="M512,0 C566,150 566,320 470,482 L506,482 C600,320 598,150 546,0 Z" fill="var(--green)"/>
    <path d="M528,302 C700,306 860,304 1024,296 L1024,482 L496,482 C520,420 530,360 528,302 Z" fill="var(--charcoal)"/>
    <path d="M528,302 C700,306 860,304 1024,296" fill="none" stroke="var(--green)" stroke-width="3"/>
  </svg>

  <h2 class="abs services-title">SERVICES:</h2>
  <ul class="abs services-list">
    <li>6 monthly Maintainence</li>
    <li>CAD/CAM Dentistry</li>
    <li>Conscious Sedation</li>
    <li>Cosmetic Dentistry</li>
    <li>Crowns and Bridges</li>
    <li>Dental Implant</li>
    <li>Fissure Sealants</li>
    <li>Tresluxa</li>
    <li>Periodontal Treatment</li>
    <li>Root Canal Treatment</li>
    <li>Teeth Whitening</li>
    <li>Tooth Coloured Fillings</li>
    <li>Tooth Replacement</li>
  </ul>

  <div class="abs hours">
    <h3>Opening Hours</h3>
    <table>
      <tr><td>Mon/Wed:</td><td>8:30AM - 5PM</td></tr>
      <tr><td>Thursday:</td><td>9:00AM - 7PM</td></tr>
      <tr><td>Friday:</td><td>9:00AM - 5PM</td></tr>
      <tr><td>Saturday:</td><td>9:00AM - 1PM</td></tr>
    </table>
  </div>
  <p class="abs saturday-note">Open on Saturdays</p>
  <span class="abs icon-badge back-phone-icon"><svg viewBox="0 0 24 24"><path fill="#fff" d="M6.6 10.8a15 15 0 0 0 6.6 6.6l2.2-2.2a1 1 0 0 1 1-.25 11.4 11.4 0 0 0 3.6.57 1 1 0 0 1 1 1V20a1 1 0 0 1-1 1A17 17 0 0 1 3 4a1 1 0 0 1 1-1h3.5a1 1 0 0 1 1 1c0 1.25.2 2.45.57 3.57a1 1 0 0 1-.25 1z"/></svg></span>
  <p class="abs back-phone">07-5019 4427</p>

  <div class="abs brand back-brand">
    <span class="brand-dot"></span>
    <span class="brand-name">Willowbay Dental<br>Centre</span>
  </div>

  <div class="abs contact-row contact-address">
    <span class="icon-badge"><svg viewBox="0 0 24 24"><path fill="#fff" d="M12 2a7 7 0 0 0-7 7c0 5 7 13 7 13s7-8 7-13a7 7 0 0 0-7-7zm0 9.5A2.5 2.5 0 1 1 12 6.5a2.5 2.5 0 0 1 0 5z"/></svg></span>
    <span>Willowbay Dental Centre Tarrawin<br>318D, Pellam Street, Tarrawin - 4587</span>
  </div>
  <div class="abs contact-row contact-email">
    <span class="icon-badge"><svg viewBox="0 0 24 24"><rect x="3" y="6" width="18" height="12" rx="1" fill="none" stroke="#fff" stroke-width="2"/><path d="M3 7l9 6 9-6" fill="none" stroke="#fff" stroke-width="2"/></svg></span>
    <span>admin@willowbaydentalcentretarrawin.com.au</span>
  </div>
  <div class="abs contact-row contact-web">
    <span class="icon-badge"><svg viewBox="0 0 24 24"><circle cx="12" cy="12" r="9" fill="none" stroke="#fff" stroke-width="2"/><path d="M3 12h18M12 3c3 3 3 15 0 18M12 3c-3 3-3 15 0 18" fill="none" stroke="#fff" stroke-width="1.6"/></svg></span>
    <span>www.willowbaydentalcentretarrawin.com.au</span>
  </div>
</section>

</body>
</html>
```